Business cards, stationary & real estate signs
LT&R Design
Business cards, stationary & real estate signs -
Creative Brief
Bright & Fun-filled
Joan V. Marsh
Broker, Realtor, CSP
4821 Tindall Lane, Suite 118 Wake Forest, NC 27587
joan@gretaholmvale.example
www.joan.quadranthousefinder.example
In addition to business card and stationary we would also like a design for our real estate signs using the colors on our logo. The signs will be mounted to posts and will be 30x24in

```html
<!DOCTYPE html>
<html lang="en">
<head>
<meta charset="utf-8">
<title>LT&amp;R Design – Stationery Set</title>
<link href="https://fonts.googleapis.com/css2?family=Open+Sans:wght@400;600;700&display=swap" rel="stylesheet">
<style>
  :root {
    --lime: #9cc63b;
    --teal: #1d5f7d;
    --ink: #4a4a4a;
    --muted: #8a8a8a;
    --paper: #ffffff;
    --backdrop: #e6e6e4;
    --body-font: "Open Sans", Arial, sans-serif;
  }
  * { box-sizing: border-box; margin: 0; padding: 0; }
  html, body { width: 1200px; height: 631px; overflow: hidden; }
  body { background: var(--backdrop); font-family: var(--body-font); color: var(--ink); position: relative; }

  .sheet { position: absolute; background: var(--paper); box-shadow: 0 2px 6px rgba(0,0,0,.18); overflow: hidden; }

  /* Company name set plainly in the body font, one colour, one weight */
  .brand { display: flex; align-items: center; gap: 6px; font-family: var(--body-font); font-weight: 600; color: var(--ink); white-space: nowrap; letter-spacing: .02em; }
  .brand-mark { background: var(--lime); flex: none; border-radius: 50%; }

  .band { position: absolute; left: 0; right: 0; background: var(--lime); }

  /* Envelope front */
  .envelope-front { left: 29px; top: 14px; width: 330px; height: 214px; }
  .envelope-front .band-top { top: 0; height: 30px; }
  .envelope-front .band-bottom { bottom: 0; height: 22px; display: flex; align-items: center; justify-content: space-between; padding: 0 10px; color: #fff; font-size: 6px; }
  .envelope-front .brand { position: absolute; left: 50%; top: 38px; transform: translateX(-50%); font-size: 15px; }
  .envelope-front .brand-mark { width: 9px; height: 9px; }

  /* Envelope back */
  .envelope-back { left: 29px; top: 240px; width: 340px; height: 132px; }
  .envelope-back .flap { position: absolute; left: 0; top: 0; width: 100%; height: 100%; }

  /* Small business cards */
  .card-small { top: 386px; width: 160px; height: 128px; }
  .card-contact { left: 29px; }
  .card-contact .band-bottom { bottom: 0; height: 16px; display: flex; align-items: center; padding: 0 8px; color: #fff; font-size: 5px; white-space: nowrap; }
  .contact-list { list-style: none; position: absolute; left: 10px; top: 18px; font-size: 6px; line-height: 15px; }
  .contact-list li { display: flex; align-items: center; gap: 4px; white-space: nowrap; }
  .icon-dot { width: 9px; height: 9px; flex: none; }
  .card-name-side { position: absolute; right: 8px; top: 18px; text-align: right; }
  .card-name-side .name { font-size: 6.5px; font-weight: 700; color: var(--teal); }
  .card-name-side .role { font-size: 5px; color: var(--muted); }

  .card-logo { left: 202px; }
  .card-logo .band-top { top: 0; height: 28px; display: flex; align-items: center; justify-content: flex-end; padding: 0 10px; }
  .card-logo .band-top .name { color: #fff; font-size: 8px; font-weight: 700; }
  .card-logo .brand { position: absolute; left: 50%; top: 56px; transform: translateX(-50%); font-size: 12px; }
  .card-logo .brand-mark { width: 8px; height: 8px; }
  .card-logo .band-bottom { bottom: 0; height: 14px; }

  /* Letterhead */
  .letterhead { left: 384px; top: 12px; width: 344px; height: 606px; }
  .letterhead .band-top { top: 0; height: 22px; }
  .letterhead .band-bottom { bottom: 0; height: 22px; display: flex; align-items: center; justify-content: space-between; padding: 0 14px; color: #fff; font-size: 6px; }
  .letterhead .brand { position: absolute; left: 50%; top: 32px; transform: translateX(-50%); font-size: 16px; }
  .letterhead .brand-mark { width: 9px; height: 9px; }
  .letter-body { position: absolute; left: 30px; right: 30px; top: 92px; font-size: 7px; line-height: 11px; color: var(--ink); }
  .letter-body .recipient { margin-bottom: 14px; }
  .letter-body p { margin-bottom: 11px; }
  .letter-body .closing { margin-top: 18px; }
  .letter-body .signer { margin-top: 26px; }

  /* Large business cards */
  .card-large-front { left: 768px; top: 14px; width: 420px; height: 244px; }
  .card-large-front .phones { position: absolute; left: 26px; top: 26px; list-style: none; font-size: 12px; line-height: 22px; color: var(--teal); }
  .card-large-front .phones li { display: flex; align-items: center; gap: 8px; }
  .card-large-front .phones .icon-dot { width: 14px; height: 14px; }
  .card-large-front .name { position: absolute; right: 26px; top: 28px; font-size: 14px; font-weight: 700; color: var(--teal); }
  .card-large-front .brand { position: absolute; right: 26px; top: 110px; font-size: 22px; }
  .card-large-front .brand-mark { width: 13px; height: 13px; }
  .card-large-front .band-bottom { bottom: 0; height: 40px; display: flex; align-items: center; justify-content: flex-end; padding: 0 26px; color: #fff; font-size: 12px; font-weight: 600; }

  .card-large-back { left: 912px; top: 300px; width: 276px; height: 316px; }
  .card-large-back .band-top { top: 0; height: 46px; display: flex; align-items: center; padding: 0 20px; color: #fff; font-size: 14px; font-weight: 700; }
  .card-large-back .brand { position: absolute; left: 50%; top: 104px; transform: translateX(-50%); font-size: 20px; }
  .card-large-back .brand-mark { width: 12px; height: 12px; }
  .card-large-back .phones { position: absolute; left: 24px; top: 190px; list-style: none; font-size: 11px; line-height: 24px; color: var(--teal); }
  .card-large-back .phones li { display: flex; align-items: center; gap: 8px; }
  .card-large-back .phones .icon-dot { width: 14px; height: 14px; }
  .card-large-back .band-bottom { bottom: 0; height: 16px; }
</style>
</head>
<body>

<svg width="0" height="0" style="position:absolute">
  <defs>
    <symbol id="icon-phone" viewBox="0 0 20 20">
      <circle cx="10" cy="10" r="10" fill="#9cc63b"/>
      <path d="M7 5.5l2 2-1.2 1.4c.7 1.4 1.8 2.5 3.3 3.3L12.5 11l2 2-1.5 1.7C9.5 14.2 5.8 10.5 5.3 7z" fill="#fff"/>
    </symbol>
    <symbol id="icon-mail" viewBox="0 0 20 20">
      <circle cx="10" cy="10" r="10" fill="#9cc63b"/>
      <rect x="5" y="6.5" width="10" height="7" fill="none" stroke="#fff" stroke-width="1.2"/>
      <path d="M5 6.5l5 4 5-4" fill="none" stroke="#fff" stroke-width="1.2"/>
    </symbol>
  </defs>
</svg>

<section class="sheet envelope-front">
  <div class="band band-top"></div>
  <div class="brand"><span class="brand-mark"></span>LT&amp;R Design</div>
  <div class="band band-bottom">
    <span>4821 Tindall Lane, Suite 118 Wake Forest, NC 27587</span>
    <span>www.joan.quadranthousefinder.example</span>
  </div>
</section>

<section class="sheet envelope-back">
  <svg class="flap" viewBox="0 0 340 132" preserveAspectRatio="none">
    <path d="M0 0 L170 58 L340 0 L340 14 L170 72 L0 14 Z" fill="#9cc63b"/>
  </svg>
</section>

<section class="sheet card-small card-contact">
  <ul class="contact-list">
    <li><svg class="icon-dot"><use href="#icon-phone"/></svg>919-555-0142</li>
    <li><svg class="icon-dot"><use href="#icon-phone"/></svg>919-555-0187</li>
    <li><svg class="icon-dot"><use href="#icon-mail"/></svg>joan@gretaholmvale.example</li>
  </ul>
  <div class="card-name-side">
    <div class="name">Joan V. Marsh</div>
    <div class="role">Broker, Realtor, CSP</div>
  </div>
  <div class="band band-bottom">4821 Tindall Lane, Suite 118 Wake Forest, NC 27587</div>
</section>

<section class="sheet card-small card-logo">
  <div class="band band-top"><span class="name">Joan V. Marsh</span></div>
  <div class="brand"><span class="brand-mark"></span>LT&amp;R Design</div>
  <div class="band band-bottom"></div>
</section>

<section class="sheet letterhead">
  <div class="band band-top"></div>
  <div class="brand"><span class="brand-mark"></span>LT&amp;R Design</div>
  <div class="letter-body">
    <div class="recipient">Jordan Ellis<br>118 Laurel Street<br>Raleigh, NC 27601</div>
    <p>Dear Jordan Ellis,</p>
    <p>Thank you for considering our team for your next home search. We listen closely, plan each step with care, and keep you informed from the first visit until the keys are in your hand.</p>
    <p>Our agents know the neighborhoods of Wake Forest well. We compare recent sales, review every detail of a listing, and help you make a confident offer that fits your budget and your plans.</p>
    <p>When you are ready to sell, we prepare a clear marketing plan, arrange photos and showings, and negotiate firmly on your behalf so the process stays simple and calm.</p>
    <p>Please call or write any time. We look forward to working with you.</p>
    <div class="closing">Yours sincerely,</div>
    <div class="signer">Joan V. Marsh</div>
  </div>
  <div class="band band-bottom">
    <span>4821 Tindall Lane, Suite 118 Wake Forest, NC 27587</span>
    <span>www.joan.quadranthousefinder.example</span>
  </div>
</section>

<section class="sheet card-large-front">
  <ul class="phones">
    <li><svg class="icon-dot"><use href="#icon-phone"/></svg>919-555-0142</li>
    <li><svg class="icon-dot"><use href="#icon-phone"/></svg>919-555-0187</li>
    <li><svg class="icon-dot"><use href="#icon-mail"/></svg>joan@gretaholmvale.example</li>
  </ul>
  <div class="name">Joan V. Marsh</div>
  <div class="brand"><span class="brand-mark"></span>LT&amp;R Design</div>
  <div class="band band-bottom">www.joan.quadranthousefinder.example</div>
</section>

<section class="sheet card-large-back">
  <div class="band band-top">Joan V. Marsh</div>
  <div class="brand"><span class="brand-mark"></span>LT&amp;R Design</div>
  <ul class="phones">
    <li><svg class="icon-dot"><use href="#icon-phone"/></svg>919-555-0142</li>
    <li><svg class="icon-dot"><use href="#icon-phone"/></svg>919-555-0187</li>
    <li><svg class="icon-dot"><use href="#icon-mail"/></svg>joan@gretaholmvale.example</li>
  </ul>
  <div class="band band-bottom"></div>
</section>

</body>
</html>
```